Commercial Real Estate Executive Recruiting Firm Needs Business Card Design

We need a business card design for BRAMLEY | Executive Recruiting - an executive recruiting firm focused exclusively on the commercial real estate industry. We place professionals ranging from Analyst to the Executive Office covering all investment/finance disciplines (acquisitions, asset management, capital markets, etc.) in all product types (office, retail, multifamily, industrial, land, etc.). We have a passion for helping people (clients and candidates) and have a reputation for being open and honest in our recruiting - and yes, very successful. We have recently developed a new logo and would like to update our business cards as well. I've uploaded some information about our company that contains the new logo.

Target Market(s)

Commercial Real Estate professionals. Primarily in the US. These are typically, smart, driven professionals with finance degrees and MBAs. Primarily men between the ages of 25 and 55.

Industry/Entity Type

Real Estate

Font styles to use
Other font styles liked:
• The font for "BRAMLEY" is Blair ITC (Medium), and "executive recruiting" is Gotham (Book).

Requirements
Must have
• I like the idea of white background on one side and solid color (blue, black, etc.) on back of card.

Would like to utilize the fonts in the logo (to the extent possible) so as to not have too many fonts on card.
Nice to have
• I think the roles (i.e., Acquisitions, Asset Management, etc.,...) is probably likely best placed on the back side of the card with the logo maybe. See attached current business card for content.

```html
<!DOCTYPE html>
<html lang="en">
<head>
<meta charset="utf-8">
<title>BRAMLEY Executive Recruiting – Business Card</title>
<link rel="stylesheet" href="https://fonts.googleapis.com/css2?family=Montserrat:ital,wght@0,400;0,500;1,400&display=swap">
<style>
  :root {
    --brand-blue: #0e5a9c;
    --brand-blue-dark: #0a4c86;
    --card-white: #ffffff;
    --stage: #e6e8ea;
    --shadow: rgba(0,0,0,0.28);
  }
  html, body {
    margin: 0;
    width: 1200px;
    height: 1000px;
    overflow: hidden;
    background: var(--stage);
  }
  .canvas {
    position: relative;
    width: 1200px;
    height: 1000px;
  }
  .card {
    position: absolute;
    top: 218px;
    width: 508px;
    height: 327px;
    background: var(--card-white);
    box-shadow: 4px 6px 10px var(--shadow);
    overflow: hidden;
  }
  .card--front { left: 72px; }
  .card--back { left: 624px; }
  .card svg { display: block; }
  .type { font-family: "Montserrat", Arial, sans-serif; fill: var(--brand-blue); }
  .band { fill: var(--brand-blue); }
  .rule { stroke: var(--card-white); stroke-width: 3; }
  .seal { fill: var(--brand-blue-dark); }
  .name { font-size: 30px; font-weight: 500; letter-spacing: -0.5px; }
  .title { font-size: 12px; font-weight: 400; letter-spacing: 4px; }
  .wordmark { fill: var(--card-white); font-weight: 400; }
  .wordmark--name { font-size: 40px; }
  .wordmark--line { font-size: 19px; }
  .contact { font-size: 18px; font-weight: 400; letter-spacing: 1.4px; }
  .contact--phone { font-size: 20px; }
  .headline { font-size: 24.5px; font-weight: 400; letter-spacing: -0.3px; }
  .tagline { font-size: 13px; font-style: italic; letter-spacing: 1.3px; }
  .roles { font-size: 14.5px; font-weight: 400; letter-spacing: 1.3px; }
</style>
</head>
<body>
<main class="canvas">

  <section class="card card--front" aria-label="Card front">
    <svg width="508" height="327" viewBox="0 0 508 327">
      <rect class="band" x="0" y="90" width="508" height="147"/>
      <line class="rule" x1="186" y1="125" x2="508" y2="125"/>
      <line class="rule" x1="186" y1="204" x2="508" y2="204"/>
      <circle class="seal" cx="63" cy="163" r="123"/>

      <text class="type name" x="350" y="64" text-anchor="end">Jordan Hale</text>
      <text class="type title" x="362" y="60">PRESIDENT</text>

      <text class="type wordmark wordmark--name" x="203" y="168" textLength="293" lengthAdjust="spacing">BRAMLEY</text>
      <text class="type wordmark wordmark--line" x="203" y="190" textLength="293" lengthAdjust="spacing">executive recruiting</text>

      <text class="type contact contact--phone" x="493" y="268" text-anchor="end">M | 214-555-0148</text>
      <text class="type contact" x="493" y="296" text-anchor="end">jordan@bramleyrecruiting.com</text>
      <text class="type contact" x="493" y="316" text-anchor="end">www.bramleyrecruiting.com</text>
    </svg>
  </section>

  <section class="card card--back" aria-label="Card back">
    <svg width="508" height="327" viewBox="0 0 508 327">
      <text class="type headline" x="14" y="36">Comercial Real Estate Recruiting</text>
      <text class="type tagline" x="58" y="55">Analyst to Executive Office Placement</text>

      <rect class="band" x="0" y="90" width="444" height="147"/>
      <line class="rule" x1="0" y1="125" x2="321" y2="125"/>
      <line class="rule" x1="0" y1="204" x2="321" y2="204"/>
      <circle class="seal" cx="444" cy="163" r="123"/>

      <text class="type roles" x="14" y="297">Acquisitions | Asset Management | Banking</text>
      <text class="type roles" x="14" y="315">Development | Capital Markets | Brokerage</text>
    </svg>
  </section>

</main>
</body>
</html>
```